Flyer für Webseitenspezialist für Chiropraktiker
Zielgruppe
Wir sind auf Webseiten für Chiropraktiker spezialisiert. Der Flyer, der erstellt werden soll, wird auf Chiropraktiker Weiterbildung ausgelegt und soll Aufmerksamkeit erzeugen.
Aufgabenstellung
Die Flyerstruktur - aufbau. Unsere Webseite ist https://heilraum-portale.de/, der Flyer soll vom CI angelehnt werden.. Bilder, falls verwendet, gerne von Orvilo Stock.

```html
<!DOCTYPE html>
<html lang="de">
<head>
<meta charset="utf-8">
<title>Chiropraktiker – Professionelle Webseite</title>
<link rel="stylesheet" href="https://fonts.googleapis.com/css2?family=Roboto+Condensed:wght@700&family=Montserrat:wght@400&family=Roboto:wght@400;700&display=swap">
<style>
  :root {
    --bg-top: #3b4bb0;
    --bg-bottom: #2f3a93;
    --white: #ffffff;
    --ribbon: #dc7590;
    --device-light: #a9b8f2;
    --device-mid: #4a6de3;
    --device-dark: #2b2a80;
  }
  * { margin: 0; padding: 0; box-sizing: border-box; }
  html, body { width: 1200px; height: 596px; overflow: hidden; }
  .flyer {
    position: relative;
    width: 1200px;
    height: 596px;
    overflow: hidden;
    background: linear-gradient(170deg, var(--bg-top) 0%, var(--bg-bottom) 100%);
    color: var(--white);
  }
  .hero-illustration {
    position: absolute;
    left: 70px;
    top: 48px;
    width: 272px;
    height: 482px;
    border-radius: 26px;
    background: linear-gradient(160deg, var(--device-light) 0%, var(--device-mid) 45%, var(--device-dark) 100%);
  }
  .headline {
    position: absolute;
    left: 425px;
    top: 83px;
    font-family: "Roboto Condensed", "Roboto", sans-serif;
    font-weight: 700;
    font-size: 56px;
    line-height: 60px;
    letter-spacing: 1px;
    white-space: nowrap;
  }
  .subline {
    position: absolute;
    left: 434px;
    top: 247px;
    font-family: "Montserrat", sans-serif;
    font-weight: 400;
    font-size: 44px;
    line-height: 50px;
    letter-spacing: 0.3px;
    white-space: nowrap;
  }
  .benefits {
    position: absolute;
    left: 440px;
    top: 328px;
    list-style: none;
    font-family: "Montserrat", sans-serif;
    font-weight: 400;
    font-size: 35px;
    line-height: 43px;
    letter-spacing: 0.3px;
    white-space: nowrap;
  }
  .benefits li { position: relative; padding-left: 36px; }
  .benefits li::before {
    content: "";
    position: absolute;
    left: 0;
    top: 26px;
    width: 5px;
    height: 5px;
    border-radius: 50%;
    background: var(--white);
  }
  .promo-ribbon, .next-arrow { position: absolute; }
  .promo-ribbon { right: 0; top: 0; width: 240px; height: 240px; }
  .next-arrow { left: 1086px; top: 488px; width: 96px; height: 84px; }
</style>
</head>
<body>
<main class="flyer">
  <div class="hero-illustration" role="img" aria-label="Illustration eines Smartphones mit einem Arzt im Kittel und Stethoskop sowie einer Profilkarte"></div>

  <h1 class="headline">Chiropraktiker, so<br>zeigt Ihr Euch richtig!</h1>
  <p class="subline">Professionelle Webseite</p>
  <ul class="benefits">
    <li>Ein ansprechendes Layout.</li>
    <li>Kunden vertrauen Gewinnen.</li>
    <li>Sichtbarkeit verbessern.</li>
    <li>Mobiles Design.</li>
  </ul>

  <svg class="promo-ribbon" viewBox="960 0 240 240" aria-label="Aktion bis zum 31.10.2023">
    <polygon points="970,0 976,0 1200,224 1200,230" fill="#ffffff"/>
    <polygon points="979,0 1136,0 1200,64 1200,221" fill="var(--ribbon)"/>
    <polygon points="1139,0 1144,0 1200,56 1200,61" fill="#ffffff"/>
    <g transform="rotate(45 1120 62.5)" fill="#ffffff" text-anchor="middle">
      <text x="1120" y="64" font-family="Roboto, sans-serif" font-weight="700" font-size="40">AKTION</text>
      <text x="1112" y="88" font-family="Roboto, sans-serif" font-weight="400" font-size="20">bis zum 31.10.2023</text>
    </g>
  </svg>

  <svg class="next-arrow" viewBox="0 0 96 84" aria-hidden="true">
    <path d="M5 4 C -2 34, 30 58, 70 64 L 68 78 L 92 56 L 64 34 L 66 48 C 34 46, 10 30, 5 4 Z"
          fill="none" stroke="#ffffff" stroke-width="2.5" stroke-linejoin="round"/>
  </svg>
</main>
</body>
</html>
```